Newly opened kids play space needs brochure to show what our space has to offer

Tri-fold color brochure with same aethetic as website (www.fernhollowplayhouse.com) that provides a comprehensive and visual overview of what our play space is comprised of. Features of the brochure should include our logo, "A Garrick and Pellinger-inspired Play Space in the Poconos", photos of: Dedicated Infant Play Area; Cafe and Free WiFi; Weekly Themed Activities; Unique Classes; Parties and Events. Photos also of our open play area with children playing within it. Info within the brochure should include our location, hours. Please take some copy from : https://www.facebook.com/fernhollowtinkerplayhouse/?ref=bookmarks
and from the Plan Your Visit part of the website. I have a lot of photos to use; is there a way to put in generic photo placeholders and I can pick which photos of mine to go into the various areas of the brochure, or if you need the photos ahead of time, please let me know the best way to proceed. I am attaching the logo files for now.

Font styles to use
Sans Serif

Colors
85cae6
cee9f5
86cfc6
cfeae6
fdf9cf
fff3d1
eaf2ce
cadf82

Requirements
Must have
• Eye catching placement of photos; color scheme similar to website and logo colors
Should not have
• Brochure should be simple, not too colorful - no primary colors, not too crowded.

```html
<!DOCTYPE html>
<html lang="en">
<head>
<meta charset="utf-8">
<title>Fern Hollow Playhouse – Tri-fold Inside Spread</title>
<link href="https://fonts.googleapis.com/css2?family=Open+Sans:wght@300;400;800&display=swap" rel="stylesheet">
<style>
  :root{
    --stage:#e6e6e6;
    --paper:#ffffff;
    --leaf:#8dc044;
    --sky:#1e9ad6;
    --rose:#e0607e;
    --ink-light:#ffffff;
    --photo-wood:#c98a5e;
    --photo-warm:#b9865f;
    --photo-navy:#1f2f63;
    --photo-soft:#d8c3ae;
  }
  *{margin:0;padding:0;box-sizing:border-box}
  html,body{width:1200px;height:800px;overflow:hidden;background:var(--stage);font-family:"Open Sans",sans-serif}
  .spread{position:absolute;left:20px;top:20px;width:1160px;height:760px;background:var(--paper);overflow:hidden;box-shadow:0 4px 16px rgba(0,0,0,.12)}
  .spread-art{position:absolute;inset:0}
  .fold{position:absolute;top:0;bottom:0;width:1px;background:rgba(0,0,0,.05)}
  .feature{position:absolute;color:var(--ink-light);width:330px}
  .feature-title{font-weight:300;font-size:30px;line-height:1.05;letter-spacing:.2px}
  .feature-title strong{font-weight:800}
  .feature-rule{width:34px;height:3px;background:var(--ink-light);margin:10px 0 12px}
  .feature-copy{font-size:14px;line-height:1.45;font-weight:400}
</style>
</head>
<body>
<main class="spread">
  <svg class="spread-art" viewBox="0 0 1160 760" width="1160" height="760">
    <!-- green feature band -->
    <path d="M0 0 H905 C860 130 800 230 700 300 C610 360 520 390 420 392 L0 392 Z" fill="var(--leaf)"/>
    <!-- top-right accent strips -->
    <path d="M905 0 H935 C890 135 830 240 735 312 L720 300 C815 228 865 125 905 0Z" fill="var(--sky)"/>
    <path d="M890 0 H905 C860 130 800 230 700 300 L690 292 C790 222 848 122 890 0Z" fill="var(--rose)"/>
    <!-- stripes under the band -->
    <path d="M0 392 H420 C520 390 610 360 700 300 L708 310 C615 372 522 402 420 404 L0 404Z" fill="var(--rose)"/>
    <path d="M0 404 H420 C522 402 615 372 708 310 L716 320 C620 384 524 414 420 416 L0 416Z" fill="var(--sky)"/>

    <!-- open play area photo with wavy edge -->
    <path d="M40 760 C140 600 300 540 430 522 C570 502 660 468 770 416 C900 356 1010 330 1160 322 V760Z" fill="var(--rose)"/>
    <path d="M62 760 C160 616 310 556 436 538 C574 518 664 484 776 432 C904 374 1012 348 1160 340 V760Z" fill="var(--sky)"/>
    <g role="img" aria-label="Photo: children playing in the open play area on a wooden floor">
      <defs>
        <linearGradient id="playFloor" x1="0" y1="0" x2="1" y2="1">
          <stop offset="0" stop-color="var(--photo-wood)"/>
          <stop offset=".55" stop-color="var(--photo-warm)"/>
          <stop offset="1" stop-color="var(--photo-navy)"/>
        </linearGradient>
      </defs>
      <path d="M84 760 C180 630 318 572 442 554 C578 534 668 500 782 448 C908 392 1014 364 1160 356 V760Z" fill="url(#playFloor)"/>
    </g>

    <!-- café photo circle -->
    <circle cx="205" cy="468" r="132" fill="var(--sky)"/>
    <circle cx="205" cy="468" r="122" fill="var(--photo-soft)" role="img" aria-label="Photo: a parent enjoying coffee at a café table"/>

    <!-- themed activities circle -->
    <circle cx="975" cy="122" r="112" fill="var(--sky)"/>
    <circle cx="975" cy="122" r="102" fill="#8a7a6a" role="img" aria-label="Photo: children planting flowers during a themed activity"/>

    <!-- infant area heart -->
    <path d="M830 445 C690 365 700 230 775 228 C808 228 826 252 830 275 C834 252 852 228 885 228 C960 230 970 365 830 445Z" fill="var(--rose)"/>
    <path d="M830 430 C705 356 714 242 777 241 C806 241 823 263 830 290 C837 263 854 241 883 241 C946 242 955 356 830 430Z" fill="#b89a86" role="img" aria-label="Photo: parent and baby in the dedicated infant area"/>

    <!-- classes circle -->
    <circle cx="1058" cy="308" r="88" fill="var(--leaf)"/>
    <circle cx="1058" cy="308" r="79" fill="#a98d78" role="img" aria-label="Photo: children and parents sitting in a circle during a class"/>
  </svg>

  <div class="fold" style="left:387px"></div>
  <div class="fold" style="left:773px"></div>

  <section class="feature" style="left:40px;top:70px">
    <h2 class="feature-title">Café and <strong>WIFI</strong></h2>
    <div class="feature-rule"></div>
    <p class="feature-copy">Take a break or catch up on work while enjoying Crema Nord coffee, beverages, and healthy snacks.</p>
  </section>

  <section class="feature" style="left:40px;top:205px">
    <h2 class="feature-title">Dedicated<br><strong>Infant Area</strong></h2>
    <div class="feature-rule"></div>
    <p class="feature-copy">Bond safely with your baby while being within eyeshot of the main play area.</p>
  </section>

  <section class="feature" style="left:420px;top:50px;width:300px">
    <h2 class="feature-title">Themed <strong>Activities</strong></h2>
    <div class="feature-rule"></div>
    <p class="feature-copy">Stories, crafts, and activities change weekly to celebrate the seasons and the world around us.</p>
  </section>

  <section class="feature" style="left:420px;top:165px;width:260px">
    <h2 class="feature-title">Unique <strong>Classes</strong></h2>
    <div class="feature-rule"></div>
    <p class="feature-copy">Our multi-age, multi-sensory approach to traditional classes nurtures the whole child in a creative and fun way.</p>
  </section>
</main>
</body>
</html>
```